Bright Path Flyer Design for Virtual Online Clinic. -5.5 x 8.5 inches (half sheet)

We need a clean, modern flyer design for Bright Path, a new virtual walk-in clinic based in British Columbia. The flyer will be used in libraries, pharmacies, and community centers to help residents easily access primary care through their Bright Path NFC access card.
The flyer will ask a question : NEED A DOCTOR? This should be large and attention grabbing.
The design should clearly feature a Bright Path card image (the access card) as the centerpiece and visually show how patients can use it to book appointments. The tone should feel trustworthy, healthcare-oriented, and community-friendly — clean fonts, clear spacing, and strong readability from a distance.

Side One: This card has the NFC Access Card.
NEED A DOCTOR? (Large Font, Attention Grabbing)
How to Book an Appointment using your Bright Path Card
Step 1: Tap Your Card on Your Phone
Hold your card near the back of your phone.
It will activate automatically — no app needed.
The Bright Path scheduler will open.
Step 2: Schedule Your Appointment
Select your clinical concern.
Choose your time window.
Register (only once).
Confirm your appointment.
Step 3: Relax, we’ll take care of the rest
A doctor will call during your scheduled time.
Once booked, you’ll be able to call our office.
No emails, no texts — just a real person.
It’s that simple.
Side Two:
About Bright Path
Created by Dr. Marcus Ferrigan
Bright Path was founded to make healthcare simple and convenient. Prescription renewals. Common infections. Medical notes. And so much more.
Our doctors can address 120+ health concerns virtually — providing quality care without the waiting room. No waiting rooms. Just real doctors providing real care.
Why Patients Choose Bright Path
Easy access – book and be seen from anywhere in BC.
Effortless booking – tap your Bright Path Card to begin.
Trusted physicians – every visit is with a licensed BC family doctor.
How It Works
Book your visit — choose a time window that fits your day.
Join the queue — you’ll be called when it’s your turn.
Speak directly with your doctor — simple, secure, and stress-free.
Convenient Care for Common Concerns

Additional Details.
Please find the domain to be launched soon. I've attached the NFC card file for review, it is 85.5 mm x 54 mm. The card will be glued to the flyer.
I've attached examples of flyers but they are not the look I am seeking and I am looking for creative solutions.
Thank you!
http://brightpath-example.test/

Adult Patients in British Columbia

Healthcare

• Looking for clean lines, uniform appearance, and high legibility i.e poppins

0054AA
0677BA
7BADD7
CADEEF
E8F1F8

• Need A Doctor?
• Elegant style, not too busy, clear layout.
• Clutter, look cheap - review examples.

```html
<!DOCTYPE html>
<html lang="en">
<head>
<meta charset="utf-8">
<title>Bright Path – Need a Doctor? Flyer</title>
<link href="https://fonts.googleapis.com/css2?family=Bebas+Neue&family=Poppins:wght@300;400;500;600;700&display=swap" rel="stylesheet">
<style>
  :root {
    --brand-blue: #0b26cf;
    --brand-blue-deep: #0820b4;
    --mint: #a7f5b9;
    --mint-line: #8fe0a5;
    --ink: #141414;
    --panel-grey: #eef1f3;
    --panel-light: #f6f8f9;
    --card-border: #cfd6dc;
    --white: #ffffff;
  }
  * { box-sizing: border-box; margin: 0; padding: 0; }
  html, body { width: 1200px; height: 1200px; overflow: hidden; background: var(--white); }
  body { position: relative; font-family: "Poppins", sans-serif; color: var(--ink); }

  .flyer-side {
    position: absolute; left: 242px; width: 724px; height: 469px;
    background: var(--white); box-shadow: 0 3px 6px rgba(0,0,0,.28); overflow: hidden;
  }
  .side-front { top: 100px; }
  .side-back { top: 609px; }

  /* FRONT */
  .hero { position: absolute; left: 0; top: 0; width: 100%; height: 272px; background: var(--brand-blue); }
  .brand-name { position: absolute; color: var(--white); font-weight: 400; letter-spacing: .5px; }
  .hero .brand-name { left: 45px; top: 36px; font-size: 22px; }
  .headline {
    position: absolute; left: 40px; top: 88px; font-family: "Bebas Neue", sans-serif;
    color: var(--white); font-size: 101px; line-height: .82; letter-spacing: -1px;
  }
  .access-card { position: absolute; left: 357px; top: 56px; width: 319px; height: 191px; background: var(--white); }
  .access-card .card-art { position: absolute; left: 10px; top: 10px; width: 150px; height: 171px; }
  .access-card .card-name { position: absolute; left: 120px; top: 68px; width: 190px; text-align: center; color: var(--brand-blue); font-size: 25px; font-weight: 400; }
  .access-card .chip-mark { position: absolute; right: 29px; top: 25px; width: 12px; height: 12px; background: var(--brand-blue); }
  .access-card .tap-label { position: absolute; left: 189px; top: 151px; font-size: 9.5px; color: var(--brand-blue); display: flex; align-items: center; gap: 7px; }
  .tap-label svg { width: 25px; height: 16px; }

  .booking-band {
    position: absolute; left: 0; top: 272px; width: 100%; height: 47px; background: var(--mint);
    color: var(--white); font-size: 19.5px; font-weight: 500; text-align: center; line-height: 47px; letter-spacing: -.1px;
  }
  .steps { position: absolute; left: 0; top: 319px; width: 100%; height: 150px; display: flex; }
  .step { flex: 1; text-align: center; padding-top: 12px; background: var(--panel-grey); }
  .step:nth-child(2) { background: var(--panel-light); }
  .step-title { display: inline-flex; align-items: center; gap: 7px; color: var(--brand-blue); font-size: 18px; font-weight: 400; height: 28px; }
  .step-title svg { width: 28px; height: 28px; }
  .step p { font-size: 9.6px; line-height: 13.3px; margin-top: 6px; padding: 0 20px; color: #1c1c1c; }

  /* BACK */
  .about { position: absolute; left: 0; top: 0; width: 251px; height: 100%; background: var(--brand-blue); color: var(--white); padding-left: 43px; }
  .about-kicker { position: absolute; left: 43px; top: 46px; font-size: 17px; font-weight: 300; }
  .about .brand-name { left: 43px; top: 70px; font-size: 27px; }
  .creator { position: absolute; left: 43px; top: 120px; font-size: 10.5px; font-weight: 300; }
  .creator strong { font-weight: 600; }
  .rule { position: absolute; left: 43px; width: 168px; height: 1px; background: linear-gradient(90deg, transparent, var(--mint-line), transparent); }
  .about-copy { position: absolute; left: 43px; width: 180px; font-size: 9.8px; line-height: 13px; font-weight: 300; }
  .stat { position: absolute; left: 43px; top: 278px; display: flex; align-items: center; gap: 8px; }
  .stat-num { font-size: 31px; font-weight: 600; line-height: 1; }
  .stat-label { font-size: 11.5px; font-weight: 600; line-height: 12.5px; }
  .site-url { position: absolute; left: 45px; top: 437px; font-size: 10px; font-weight: 600; letter-spacing: .3px; }

  .benefits { position: absolute; left: 251px; top: 0; width: 473px; height: 228px; background: var(--white); }
  .section-title { position: absolute; width: 100%; text-align: center; font-size: 22px; font-weight: 500; color: var(--ink); }
  .section-title::after { content: ""; display: block; margin: 4px auto 0; width: 140px; height: 1px; background: var(--mint-line); }
  .benefits .section-title { top: 36px; left: -7px; }
  .benefit { position: absolute; top: 121px; width: 130px; height: 94px; border: 1.5px solid var(--card-border); border-radius: 12px; background: var(--white); text-align: center; }
  .benefit-icon { position: absolute; left: 50%; top: -28px; margin-left: -27px; width: 54px; height: 54px; border-radius: 50%; background: var(--brand-blue); border: 2px solid var(--white); box-shadow: 0 0 0 1.5px var(--brand-blue); display: flex; align-items: center; justify-content: center; }
  .benefit-icon svg { width: 28px; height: 28px; }
  .benefit h3 { margin-top: 30px; font-size: 11px; font-weight: 600; }
  .benefit p { font-size: 9.5px; line-height: 13px; margin-top: 4px; padding: 0 8px; }

  .how { position: absolute; left: 251px; top: 228px; width: 473px; height: 241px; background: var(--panel-light); }
  .how .section-title { top: 14px; }
  .how-row { position: absolute; left: 22px; width: 410px; height: 41px; }
  .how-row .row-line { position: absolute; left: 20px; top: 0; width: 160px; height: 41px; border-top: 1px solid #dde2e6; border-bottom: 1px solid #dde2e6; }
  .how-num { position: absolute; left: 0; top: 6px; width: 30px; height: 30px; border-radius: 50%; background: var(--brand-blue); color: var(--white); font-size: 13px; font-weight: 500; line-height: 30px; text-align: center; }
  .how-step { position: absolute; left: 46px; top: 0; height: 41px; width: 130px; display: flex; align-items: center; font-size: 11px; font-weight: 500; line-height: 13px; }
  .how-detail { position: absolute; left: 181px; top: 0; width: 228px; height: 41px; background: var(--brand-blue); border-radius: 3px; color: var(--white); font-size: 9.8px; display: flex; align-items: center; padding-left: 13px; }
</style>
</head>
<body>

<section class="flyer-side side-front">
  <div class="hero">
    <div class="brand-name">Bright Path</div>
    <h1 class="headline">NEED A<br>DOCTOR?</h1>
    <div class="access-card">
      <svg class="card-art" viewBox="0 0 150 171" role="img" aria-label="Blue card artwork panel with brand illustration">
        <polygon points="0,0 128,0 75,60 75,171 0,171" fill="var(--brand-blue)"/>
      </svg>
      <span class="chip-mark"></span>
      <div class="card-name">Bright Path</div>
      <div class="tap-label">Tap Here to Book
        <svg viewBox="0 0 25 16" fill="none" stroke="currentColor" stroke-width="1.3">
          <rect x="1" y="2" width="13" height="12" rx="2"/>
          <path d="M17 5c1.2 1.8 1.2 4.2 0 6M20 3.5c2 2.7 2 6.3 0 9M23 2c2.6 3.6 2.6 8.4 0 12"/>
        </svg>
      </div>
    </div>
  </div>

  <div class="booking-band">HOW TO BOOK AN APPOINTMENT USING YOUR BRIGHT PATH CARD</div>

  <div class="steps">
    <div class="step">
      <div class="step-title">STEP 1
        <svg viewBox="0 0 28 28" fill="none" stroke="var(--mint-line)" stroke-width="1.2">
          <rect x="9" y="3" width="14" height="22" rx="2"/><rect x="3" y="10" width="16" height="10" rx="1.5"/>
          <path d="M24 2c1.5 1.5 1.5 4 0 5.5M26 0.5c2.3 2.3 2.3 6.2 0 8.5"/>
        </svg>
      </div>
      <p>Tap Your Card on Your Phone<br>Hold your card near the back of your phone. It will activate automatically — no app needed. The Bright Path scheduler will open.</p>
    </div>
    <div class="step">
      <div class="step-title">STEP 2
        <svg viewBox="0 0 28 28" fill="none" stroke="var(--mint-line)" stroke-width="1.2">
          <rect x="6" y="8" width="20" height="18" rx="2"/><path d="M6 13h20M10 17h2M15 17h2M20 17h2M10 21h2M15 21h2M20 21h2"/>
          <circle cx="7" cy="7" r="5.5" fill="var(--panel-light)"/><path d="M7 4v3l2 1.5"/>
        </svg>
      </div>
      <p>Schedule Your Appointment<br>Select your clinical concern.<br>Choose your time window.<br>Register (only once).<br>Confirm your appointment.</p>
    </div>
    <div class="step">
      <div class="step-title">STEP 3
        <svg viewBox="0 0 28 28" fill="none" stroke="var(--mint-line)" stroke-width="1.2">
          <rect x="4" y="6" width="13" height="20" rx="2"/><path d="M8 23h5"/>
          <rect x="17" y="1" width="10" height="8" rx="1.5"/><path d="M20 9l-2 3"/>
        </svg>
      </div>
      <p>Relax, we’ll take care of the rest<br>A doctor will call during your scheduled time. Once booked, you’ll be able to call our office. No emails, no texts — just a real person. It’s that simple.</p>
    </div>
  </div>
</section>

<section class="flyer-side side-back">
  <aside class="about">
    <div class="about-kicker">ABOUT</div>
    <div class="brand-name">Bright Path</div>
    <div class="creator">Created by <strong>Dr. Marcus Ferrigan</strong></div>
    <div class="rule" style="top:155px"></div>
    <p class="about-copy" style="top:178px">Bright Path was founded to make healthcare simple and convenient. Prescription renewals. Common infections. Medical notes. And so much more.</p>
    <div class="rule" style="top:258px"></div>
    <div class="stat"><span class="stat-num">120+</span><span class="stat-label">HEALTH<br>CONCERNS</span></div>
    <p class="about-copy" style="top:319px">Our doctors can address 120+ health concerns virtually — providing quality care without the waiting room. No waiting rooms. Just real doctors providing real care.</p>
    <div class="site-url">www.brightpath-example.test</div>
  </aside>

  <div class="benefits">
    <h2 class="section-title">Why Patients Choose Bright Path</h2>
    <div class="benefit" style="left:23px">
      <div class="benefit-icon"><svg viewBox="0 0 28 28" fill="none" stroke="#fff" stroke-width="1.4"><rect x="6" y="3" width="12" height="22" rx="2"/><rect x="11" y="9" width="13" height="9" rx="1.5"/><path d="M10 22h4"/></svg></div>
      <h3>Easy access</h3>
      <p>Book and be seen from anywhere in BC.</p>
    </div>
    <div class="benefit" style="left:152px">
      <div class="benefit-icon"><svg viewBox="0 0 28 28" fill="none" stroke="#fff" stroke-width="1.4"><rect x="10" y="4" width="15" height="10" rx="1.5" transform="rotate(-18 17 9)"/><path d="M4 24l5-7 4 1 3-3"/></svg></div>
      <h3>Effortless booking</h3>
      <p>Tap your Bright Path Card to begin.</p>
    </div>
    <div class="benefit" style="left:288px">
      <div class="benefit-icon"><svg viewBox="0 0 28 28" fill="none" stroke="#fff" stroke-width="1.4"><path d="M14 3l9 4v7c0 6-4 9-9 11-5-2-9-5-9-11V7z"/><path d="M10 14l3 3 6-6"/></svg></div>
      <h3>Trusted physicians</h3>
      <p>Every visit is with a licensed BC family doctor.</p>
    </div>
  </div>

  <div class="how">
    <h2 class="section-title">How It Works</h2>
    <div class="how-row" style="top:58px">
      <span class="row-line"></span><span class="how-num">1</span>
      <span class="how-step">Book your visit</span>
      <span class="how-detail">Choose a time window that fits your day.</span>
    </div>
    <div class="how-row" style="top:110px">
      <span class="row-line"></span><span class="how-num">2</span>
      <span class="how-step">Join the queue</span>
      <span class="how-detail">You’ll be called when it’s your turn.</span>
    </div>
    <div class="how-row" style="top:162px">
      <span class="row-line"></span><span class="how-num">3</span>
      <span class="how-step">Speak directly with your doctor</span>
      <span class="how-detail">Simple, secure, and stress-free.</span>
    </div>
  </div>
</section>

</body>
</html>
```